Faithful Harbor Fellowship Network needs a fresh new web design

We are an up and coming multicultural church that aims to bring people into a life changing encounter with God. We need a fresh and inviting website in order to increase our internet presence and make us easier to connect with.
Here are some of the basic requirements for the site:
• Clearly displayed address, service times, and contact info
• A staff profile page
• An area for a calendar with upcoming events and their details
• Social media buttons
• Group pages for the different ministries (youth, children’s church, men, etc…)
• An area for donations and eCommerce
• A resources page for assorted media (podcasts, sermons, videos, etc.…)
• An area for prayer requests.

Industry/Entity Type

Church

```html
<!DOCTYPE html>
<html lang="en">
<head>
<meta charset="utf-8">
<title>Faithful Harbor Fellowship Network – Children's Ministry</title>
<link href="https://fonts.googleapis.com/css2?family=Lato:wght@300;400;700&display=swap" rel="stylesheet">
<style>
:root{
  --royal:#1f1a9a;
  --royal-deep:#16127a;
  --gold:#e4be1c;
  --gold-text:#d6ae17;
  --page:#f1f1f1;
  --ink:#555;
  --ink-dark:#444;
  --rule:#dcdcdc;
  --white:#fff;
}
*{box-sizing:border-box;margin:0;padding:0}
html,body{width:1200px;height:2647px;overflow:hidden}
body{position:relative;background:var(--page);font-family:'Lato',sans-serif;color:var(--ink)}
.abs{position:absolute}

/* top bar */
.topbar{left:0;top:0;width:1200px;height:40px;background:var(--royal);color:var(--white);font-size:13px}
.topbar .tagline{left:100px;top:12px;white-space:nowrap}
.topbar .schedule-label{left:736px;top:12px;font-size:13px;white-space:nowrap}
.topbar .schedule{left:920px;top:4px;border-left:1px solid rgba(255,255,255,.6);padding-left:10px;font-size:12px;line-height:16px;white-space:nowrap}

/* header */
.header{left:0;top:40px;width:1200px;height:115px;background:var(--white)}
.brand{left:100px;top:30px;display:flex;align-items:center;gap:12px}
.brand-mark{width:46px;height:46px;border-radius:50%;background:var(--royal)}
.brand-name{font-size:19px;font-weight:700;color:var(--royal);line-height:22px;width:200px}
.info{top:24px;text-align:right;font-size:13px;line-height:17px;color:var(--ink-dark)}
.info h3{font-size:16px;font-weight:700;color:#444;margin-bottom:4px}
.info a{color:var(--gold-text);text-decoration:none;font-size:12px}
.info-donate{right:627px;width:230px}
.info-prayer{right:344px;width:260px}
.info-address{right:168px;width:150px}
.divider-v{top:24px;width:1px;height:70px;background:var(--rule)}
.social{left:1072px;display:block;width:28px;height:28px;border-radius:50%;background:#9a9a9a}

/* nav */
.nav{left:0;top:155px;width:1200px;height:40px;background:var(--gold);display:flex;align-items:center;padding-left:90px}
.nav a{color:var(--white);text-decoration:none;font-size:14px;padding:0 26px;border-right:1px solid rgba(255,255,255,.55);line-height:16px}
.nav a:last-child{border-right:0}

/* page banner */
.banner{left:0;top:195px;width:1200px;height:101px}
.banner-photo{left:0;top:0;width:1200px;height:101px;background:linear-gradient(90deg,#1f1906,#4a3a10 45%,#2a2108 70%,#3d300c)}
.crumbs{left:100px;top:27px;color:#e6e6e6;font-size:13px;white-space:nowrap}
.crumbs .current{color:var(--white)}
.page-title{left:100px;top:45px;color:var(--white);font-size:27px;font-weight:700;white-space:nowrap}

/* main */
.main{left:110px;top:353px;width:630px}
.quote{font-size:22px;font-weight:300;color:#555;line-height:28px}
.quote-ref{font-size:12px;color:#777;margin-top:6px}
.body-text{font-size:12.5px;line-height:20px;color:#666}
.intro p{margin-top:22px}
.section-title{font-size:25px;color:var(--gold-text);font-weight:400;text-transform:uppercase}
.level{padding:14px 0 14px;border-bottom:1px solid var(--rule)}
.level:last-child{border-bottom:0}
.level h4{font-size:19px;font-weight:400;color:#555;margin-bottom:6px}

.album{margin-top:20px}
.album-head{display:flex;justify-content:space-between;align-items:center;margin-bottom:14px}
.album-head h4{font-size:19px;font-weight:400;color:#666;text-transform:uppercase}
.pager{display:flex;gap:4px}
.pager span{width:18px;height:18px;border-radius:50%;background:var(--gold);display:block}
.pager span.off{opacity:.5}
.thumbs{display:flex;gap:11px}
.thumb{width:150px;height:86px;background:var(--white)}

/* sidebar */
.sidebar{left:788px;top:346px;width:302px}
.sidebar .section-title{font-size:25px;padding-bottom:6px;border-bottom:2px solid var(--gold)}
.news-item{margin-top:24px}
.news-item h5{font-size:17px;font-weight:700;color:#555;margin-bottom:8px}
.news-row{display:flex;gap:16px;align-items:flex-start}
.news-photo{width:121px;height:75px;background:linear-gradient(135deg,#e8c13b,#d8573a 45%,#3fa3c4)}
.news-when{color:var(--gold-text);font-size:17px;line-height:22px}

/* footer */
.footer{left:0;top:1736px;width:1200px;height:298px;background:var(--royal);color:#d8d8ef;font-size:12.5px;line-height:19px}
.col{top:50px}
.col h6{font-size:18px;font-weight:400;color:var(--white);margin-bottom:10px;text-transform:uppercase}
.contact-line{display:flex;align-items:center;gap:10px;margin-top:4px}
.communities{display:grid;grid-template-columns:110px 110px;row-gap:4px}
.communities li{list-style:none}
.communities li.item::before{content:"• "}
.email-field{width:226px;height:34px;background:var(--white);border-radius:3px;color:#aaa;padding:8px 12px;margin-top:6px}
.subscribe{display:inline-block;background:var(--gold);color:var(--white);padding:7px 16px;border-radius:3px;margin-top:12px}
.footer-social{display:flex;gap:8px;margin-top:10px}
.footer-social span{width:32px;height:32px;border-radius:50%;background:#9a9ac9;display:block}
.footer-rule{left:110px;top:223px;width:980px;height:1px;background:rgba(255,255,255,.18)}
.copyright{left:0;top:245px;width:1200px;text-align:center;font-size:12px;color:#bdbde6}

/* lightbox state */
.lightbox-stage{left:0;top:2034px;width:1200px;height:613px;background:var(--gold)}
.ghost{left:110px;top:55px;width:630px;opacity:.12}
.ghost .thumb{background:#000}
.lightbox{left:150px;top:183px;width:551px;height:313px;background:var(--royal);padding:14px}
.lightbox-photo{width:100%;height:100%;background:linear-gradient(120deg,#d9c5a8,#f3e3cf 40%,#c98c57 75%,#e9d7bb)}
.lb-arrow{top:123px;width:34px;height:52px;background:var(--royal);display:flex;align-items:center;justify-content:center}
.lb-prev{left:0;border-radius:0 26px 26px 0}
.lb-next{right:0;border-radius:26px 0 0 26px}
</style>
</head>
<body>

<div class="abs topbar">
  <span class="abs tagline">A house of prayer for all nations, where the love, the presence and the power of God are real.</span>
  <span class="abs schedule-label">SUNDAY SERVICE SCHEDULE</span>
  <div class="abs schedule">09:00 A.M. | Sunday School<br>10:30 A.M. | Convergent Service</div>
</div>

<header class="abs header">
  <div class="abs brand">
    <span class="brand-mark"></span>
    <span class="brand-name">Faithful Harbor Fellowship Network</span>
  </div>
  <div class="abs info info-donate"><h3>Donate</h3>Lorem Ipsum is simply<br>dummy text of the printing<br><a href="#">Donate Now »</a></div>
  <div class="abs divider-v" style="left:596px"></div>
  <div class="abs info info-prayer"><h3>Request Prayer</h3>Lorem Ipsum is simply dummy text<br>of the printing and typesetting industry.<br><a href="#">Request Now »</a></div>
  <div class="abs divider-v" style="left:876px"></div>
  <div class="abs info info-address"><h3>Address</h3>Faithful Harbor<br>City, Location<br><a href="#">Contact »</a></div>
  <span class="abs social" style="top:30px"></span>
  <span class="abs social" style="top:64px"></span>
</header>

<nav class="abs nav">
  <a href="#">Home</a><a href="#">About</a><a href="#">Staff Profile</a><a href="#">News and Events</a><a href="#">Worship &amp; Services</a><a href="#">Groups</a><a href="#">Shop</a><a href="#">Resources</a><a href="#">Contact</a>
</nav>

<div class="abs banner">
  <div class="abs banner-photo" role="img" aria-label="Dark golden header photograph"></div>
  <div class="abs crumbs">Home &gt; Groups &gt; <span class="current">Children's Ministry</span></div>
  <h1 class="abs page-title">Children's Ministry</h1>
</div>

<main class="abs main">
  <p class="quote">“Start children off on the way they should go, and even when they are old they will not turn from it.”</p>
  <p class="quote-ref">Proverbs 22:6</p>
  <div class="intro body-text">
    <p style="margin-top:34px">Lorem Ipsum is simply dummy text of the printing and typesetting industry. Lorem Ipsum has been the industry's standard dummy text ever since the 1500s, when an unknown printer took a galley of type and scrambled it to make a type specimen book It has survived not only five centuries.</p>
    <p>Also the leap into electronic typesetting, remaining essentially unchanged. It was popularised in the 1960s with the release of Lettersheet sheets containing Lorem Ipsum passages, and more recently with desktop publishing software like PageForge including versions of Lorem Ipsum.</p>
  </div>

  <h2 class="section-title" style="margin-top:44px">Class Levels</h2>
  <div class="levels body-text">
    <div class="level"><h4>LEVEL1 &nbsp;AGE 3-5</h4>Lorem Ipsum is simply dummy text of the printing and typesetting industry. Lorem Ipsum has been the industry's standard dummy text ever since the 1500s, when an unknown printer took a galley of type and scrambled it to make a type specimen book It has survived not only five centuries.</div>
    <div class="level"><h4>LEVEL2 &nbsp;AGE 6-9</h4>Lorem Ipsum is simply dummy text of the printing and typesetting industry. Lorem Ipsum has been the industry's standard dummy text ever since the 1500s, when an unknown printer took a galley of type and scrambled it to make a type specimen book It has survived not only five centuries.</div>
    <div class="level"><h4>LEVEL3 &nbsp;AGE 10-15</h4>Lorem Ipsum is simply dummy text of the printing and typesetting industry. Lorem Ipsum has been the industry's standard dummy text ever since the 1500s, when an unknown printer took a galley of type and scrambled it to make a type specimen book It has survived not only five centuries.</div>
    <div class="level"><h4>LEVEL4 &nbsp;AGE 15 AND ABOVE</h4>Lorem Ipsum is simply dummy text of the printing and typesetting industry. Lorem Ipsum has been the industry's standard dummy text ever since the 1500s, when an unknown printer took a galley of type and scrambled it to make a type specimen book It has survived not only five centuries.</div>
  </div>

  <h2 class="section-title" style="margin-top:30px">Gallery</h2>
  <div class="album">
    <div class="album-head"><h4>2014 Easter Celebration</h4><div class="pager"><span class="off"></span><span></span></div></div>
    <div class="thumbs"><div class="thumb"></div><div class="thumb"></div><div class="thumb"></div><div class="thumb"></div></div>
  </div>
  <div class="album" style="margin-top:36px">
    <div class="album-head"><h4>Lorem Ipsum</h4><div class="pager"><span class="off"></span><span></span></div></div>
    <div class="thumbs"><div class="thumb"></div><div class="thumb"></div><div class="thumb"></div><div class="thumb"></div></div>
  </div>
  <div class="album" style="margin-top:36px">
    <div class="album-head"><h4>Lorem Ipsum is simply dummy text</h4></div>
    <div class="thumbs"><div class="thumb"></div><div class="thumb"></div><div class="thumb"></div></div>
  </div>
</main>

<aside class="abs sidebar">
  <h2 class="section-title">News &amp; Events</h2>
  <div class="news-item">
    <h5>Vacation Bible School Jul15-Aug15</h5>
    <p class="body-text">Lorem Ipsum has been the industry's standard dummy text ever since the 1500s, when an unknown printer took a galley of type and scrambled it to make a type specimen book.</p>
  </div>
  <div class="news-item" style="margin-top:30px">
    <div class="news-row">
      <div class="news-photo" role="img" aria-label="Colourful children's painting activity photo"></div>
      <div><h5 style="margin-bottom:4px">Painting Competition</h5><p class="news-when">Age 5 to 15<br>on Aug15th @10am</p></div>
    </div>
    <p class="body-text" style="margin-top:16px">Lorem Ipsum has been the industry's standard dummy text ever since the 1500s, when an unknown printer took a galley of type and scrambled it to make a type specimen book.</p>
  </div>
</aside>

<footer class="abs footer">
  <div class="abs col" style="left:110px">
    <h6>Contact Us</h6>
    Faithful Harbor<br>Location,city<br>State Name, Country
    <div class="contact-line" style="margin-top:8px"><svg width="14" height="14" viewBox="0 0 14 14"><path d="M3 1l2 3-1.3 1.3a8 8 0 0 0 5 5L10 9l3 2-1 2.5C6 13 1 8 .5 2z" fill="#d8d8ef"/></svg>+1 555-014-2290</div>
    <div class="contact-line"><svg width="14" height="10" viewBox="0 0 14 10"><rect x=".5" y=".5" width="13" height="9" fill="none" stroke="#d8d8ef"/><path d="M.5 .5l6.5 5 6.5-5" fill="none" stroke="#d8d8ef"/></svg>hello@faithfulharbor.org</div>
  </div>
  <div class="abs col" style="left:331px">
    <h6>Communities We Serve</h6>
    <ul class="communities">
      <li class="item">Lorem Ipsum</li><li class="item">type text dummy</li>
      <li class="item">Dummy Links</li><li class="item">Lorem Ipsum</li>
      <li class="item">More dummy</li><li></li>
      <li class="item">Sample Text</li><li></li>
      <li class="item">More samples</li>
    </ul>
  </div>
  <div class="abs col" style="left:609px">
    <h6>Newsletter</h6>
    Enter your email below to get notified
    <div class="email-field">Your Email</div>
    <span class="subscribe">Subscribe</span>
  </div>
  <div class="abs col" style="left:887px">
    <h6>Connect With Us</h6>
    Stay connected for the latest updates at<br>Harbor Community Chapel
    <div class="footer-social"><span></span><span></span></div>
  </div>
  <div class="abs footer-rule"></div>
  <p class="abs copyright">Copyright © 2014. All rights reserved. Faithful Harbor.</p>
</footer>

<section class="abs lightbox-stage">
  <div class="abs ghost">
    <h2 class="section-title" style="color:#000">Gallery</h2>
    <div class="album">
      <div class="album-head"><h4 style="color:#000">2014 Easter Celebration</h4><div class="pager"><span style="background:#000"></span><span style="background:#000"></span></div></div>
      <div class="thumbs"><div class="thumb"></div><div class="thumb"></div><div class="thumb"></div><div class="thumb"></div></div>
    </div>
    <div class="album" style="margin-top:36px">
      <div class="album-head"><h4 style="color:#000">Lorem Ipsum</h4></div>
      <div class="thumbs"><div class="thumb"></div><div class="thumb"></div><div class="thumb"></div><div class="thumb"></div></div>
    </div>
    <div class="album" style="margin-top:36px">
      <div class="album-head"><h4 style="color:#000">Lorem Ipsum</h4></div>
      <div class="thumbs"><div class="thumb"></div><div class="thumb"></div><div class="thumb"></div></div>
    </div>
  </div>
  <div class="abs lightbox">
    <div class="lightbox-photo" role="img" aria-label="Gallery photo of children enjoying a meal together"></div>
    <span class="abs lb-arrow lb-prev"><svg width="10" height="16" viewBox="0 0 10 16"><path d="M8 2L2 8l6 6" fill="none" stroke="#fff" stroke-width="2.5"/></svg></span>
    <span class="abs lb-arrow lb-next"><svg width="10" height="16" viewBox="0 0 10 16"><path d="M2 2l6 6-6 6" fill="none" stroke="#fff" stroke-width="2.5"/></svg></span>
  </div>
</section>

</body>
</html>
```